Redesign Of Current Landing Page

I need to redesign this landing page https://www.bluewillowpromos.example/?page=landing&landing=23 (Please do not opt in because when you do it will show you the home page. Please clear your cookies before going to this url above to view the 1 page landing page.)

Please use my updated website as a reference for colors and logo.
http://sitecraftorly.example/dh/bwpg/index.html

I would like the call to action to be a button that opens into a lead form...

Button would be "Download Samples"

Target Market(s)

small business owners

Industry/Entity Type

Marketing

Number of Pages Required

1 page

Colors

Designer to choose colors to be used in the design.

Requirements
Must have
• must be full responsive on all devices
Nice to have
• must have a legitimate professional apeal to it
Should not have
• open

```html
<!DOCTYPE html>
<html lang="en">
<head>
<meta charset="utf-8">
<title>Blue Willow Promotions Group — Attract More Customers</title>
<link href="https://fonts.googleapis.com/css2?family=Lato:wght@400;700;900&display=swap" rel="stylesheet">
<style>
:root{
  --blue:#1a73c2;
  --orange:#f6a51d;
  --ink:#333333;
  --grey-bg:#f1f1f1;
  --footer-bg:#d4d4d4;
  --white:#ffffff;
}
*{margin:0;padding:0;box-sizing:border-box}
html,body{width:1200px;height:2635px;overflow:hidden;background:var(--white)}
body{font-family:'Lato',sans-serif;color:var(--ink);position:relative}

.hero{position:absolute;left:0;top:0;width:1200px;height:662px;
  background:linear-gradient(180deg,#4f5fa6 0%,#7a7fbf 35%,#8b7a86 60%,#a07a5a 78%,#3c6f8f 100%)}
.brand{position:absolute;left:137px;top:42px;font-weight:700;font-size:22px;color:var(--white);letter-spacing:.3px}
.hero-panel{position:absolute;left:137px;top:216px;width:402px;height:299px;
  background:rgba(70,70,80,.72);border:1px solid rgba(255,255,255,.35);padding:26px 28px 0 28px}
.hero-title{color:var(--white);font-weight:900;font-size:37px;line-height:44px;text-transform:uppercase}
.hero-sub{color:var(--white);font-size:22px;line-height:27px;margin-top:4px;margin-left:4px}
.cta{position:absolute;left:32px;top:209px;width:332px;height:55px;background:var(--orange);
  color:#2a2a2a;font-weight:700;font-size:21px;display:flex;align-items:center;justify-content:center;text-transform:uppercase;letter-spacing:.3px}

.why{position:absolute;left:0;top:662px;width:1200px;height:494px;background:var(--white)}
.section-title{color:var(--blue);font-weight:900;font-size:29px;line-height:36px;text-transform:uppercase;text-align:center}
.why .section-title{position:absolute;left:0;right:0;top:68px}
.benefit{position:absolute;top:210px;width:170px;text-align:center}
.benefit-icon{width:133px;height:133px;border-radius:50%;border:1.5px solid var(--blue);margin:0 auto;display:flex;align-items:center;justify-content:center}
.benefit-icon svg{width:66px;height:66px;fill:var(--blue)}
.benefit-label{margin-top:38px;font-size:12px;line-height:18px;color:#222}

.imagine{position:absolute;left:0;top:1156px;width:1200px;height:506px;background:var(--grey-bg)}
.imagine .section-title{position:absolute;left:130px;top:56px;text-align:left}
.imagine-box{position:absolute;left:132px;top:123px;width:571px;height:302px;border:2px solid #e6e6e6;background:#f3f3f3;padding:28px 44px 0 36px}
.imagine-box p{font-size:14.5px;line-height:23px;color:var(--ink);margin-bottom:22px}
.samples-art{position:absolute;left:708px;top:112px;width:408px;height:334px;
  background:linear-gradient(135deg,#2e5c9a 0%,#3c7a5e 45%,#7a2e3a 80%,#2a2a3a 100%);border-radius:4px}

.how{position:absolute;left:0;top:1662px;width:1200px;height:434px;
  background:linear-gradient(180deg,#2a78c0 0%,#1f73c0 60%,#2f86cc 100%)}
.how .section-title{position:absolute;left:0;right:0;top:77px;color:var(--orange)}
.how-copy{position:absolute;left:252px;top:158px;width:700px;text-align:center;color:var(--white);font-size:14px;line-height:28px}
.how-copy p+p{margin-top:33px}

.testimonials{position:absolute;left:0;top:2096px;width:1200px;height:474px;background:var(--white)}
.testimonials .section-title{position:absolute;left:0;right:0;top:74px}
.quote-mark{position:absolute;font-family:Georgia,serif;font-size:64px;line-height:1;color:#333;font-weight:700}
.quote-open{left:288px;top:136px}
.quote-close{left:798px;top:318px}
.quote-text{position:absolute;left:318px;top:167px;width:568px;text-align:center;font-size:14px;line-height:28px;color:#444}
.quote-name{position:absolute;left:0;right:0;top:368px;text-align:center;font-size:11px;font-weight:700;color:var(--blue)}
.quote-place{position:absolute;left:0;right:0;top:387px;text-align:center;font-size:11px;color:#555}

.site-footer{position:absolute;left:0;top:2570px;width:1200px;height:65px;background:var(--footer-bg);
  display:flex;align-items:center;justify-content:center;font-size:11px;color:#555}
</style>
</head>
<body>

<header class="hero" role="img" aria-label="Photo of a luxury villa with a lit pool at dusk">
  <div class="brand">Blue Willow</div>
  <div class="hero-panel">
    <h1 class="hero-title">Attract More<br>Customers</h1>
    <p class="hero-sub">who spend more money with your business more often!</p>
    <a class="cta">Download Samples</a>
  </div>
</header>

<section class="why">
  <h2 class="section-title">Why Offer Incentives<br>to Customers?</h2>

  <div class="benefit" style="left:105px">
    <div class="benefit-icon"><svg viewBox="0 0 64 64"><path d="M8 4h3v50h50v3H8z"/><rect x="18" y="38" width="6" height="12"/><rect x="28" y="32" width="6" height="18"/><rect x="38" y="26" width="6" height="24"/><rect x="48" y="20" width="6" height="30"/><path d="M16 34l12-10 10 6 16-16-2-2 6-1-1 6-2-2-19 19-10-6-8 8z"/></svg></div>
    <p class="benefit-label">Increase Responses<br>From Your Existing Ads</p>
  </div>
  <div class="benefit" style="left:266px">
    <div class="benefit-icon"><svg viewBox="0 0 64 64"><path d="M24 10l4 0 1 5 4 2 4-3 3 3-3 4 2 4 5 1v4l-5 1-2 4 3 4-3 3-4-3-4 2-1 5h-4l-1-5-4-2-4 3-3-3 3-4-2-4-5-1v-4l5-1 2-4-3-4 3-3 4 3 4-2z"/><circle cx="26" cy="27" r="5" fill="#fff"/><path d="M46 34h3l1 3 3 1 2-2 2 2-2 2 1 3 3 1v3l-3 1-1 3 2 2-2 2-2-2-3 1-1 3h-3l-1-3-3-1-2 2-2-2 2-2-1-3-3-1v-3l3-1 1-3-2-2 2-2 2 2 3-1z"/><circle cx="47.5" cy="45.5" r="3.5" fill="#fff"/></svg></div>
    <p class="benefit-label">#1 Sales Closing Tool -<br>Gift w/ Purchase</p>
  </div>
  <div class="benefit" style="left:426px">
    <div class="benefit-icon"><svg viewBox="0 0 64 64"><path d="M22 36l-8 22 8-4 4 7 6-18zM42 36l8 22-8-4-4 7-6-18z"/><circle cx="32" cy="24" r="18"/><circle cx="32" cy="24" r="12" fill="#fff"/><path d="M32 16l2.4 5 5.4.6-4 3.7 1.1 5.3-4.9-2.7-4.9 2.7 1.1-5.3-4-3.7 5.4-.6z"/></svg></div>
    <p class="benefit-label">Build Brand<br>Awareness and Trust</p>
  </div>
  <div class="benefit" style="left:593px">
    <div class="benefit-icon"><svg viewBox="0 0 64 64"><path d="M32 6l14 5v11c0 10-6 16-14 20-8-4-14-10-14-20V11z"/><path d="M6 30h5l6 14 8 4v10H14L6 46zM58 30h-5l-6 14-8 4v10h11l8-12z"/></svg></div>
    <p class="benefit-label">Insure The Sale Over<br>Your Competition</p>
  </div>
  <div class="benefit" style="left:760px">
    <div class="benefit-icon"><svg viewBox="0 0 64 64"><rect x="2" y="20" width="10" height="22"/><rect x="52" y="20" width="10" height="22"/><path d="M12 22l10-4 8 3 8-4 14 5v16l-6 6-4-4 3-3-14-12-6 4-4-2 8-6-6-2-11 4z"/><path d="M14 40l4 4 3-3 4 4 3-3 4 4 3-3 4 4 3-3-12-12-4 3c-3 2-6 0-6-2l5-4-13 5z"/></svg></div>
    <p class="benefit-label">Boost Repeat and<br>Referral Business-</p>
  </div>
  <div class="benefit" style="left:922px">
    <div class="benefit-icon"><svg viewBox="0 0 64 64"><path d="M32 6a26 26 0 0 1 24 16l4-2-2 12-10-6 4-2A20 20 0 0 0 14 24l-5-2A26 26 0 0 1 32 6zM32 58A26 26 0 0 1 8 42l-4 2 2-12 10 6-4 2a20 20 0 0 0 38-2l5 2A26 26 0 0 1 32 58z"/><circle cx="32" cy="32" r="12" fill="none" stroke="#1a73c2" stroke-width="2.5"/><text x="32" y="39" font-size="18" font-family="Lato,sans-serif" font-weight="700" text-anchor="middle">$</text></svg></div>
    <p class="benefit-label">Improve<br>Retention Rates</p>
  </div>
</section>

<section class="imagine">
  <h2 class="section-title">Imagine</h2>
  <div class="imagine-box">
    <p>Being able to create exciting give away promotions that will boost your sales without ever having to worry about cost.</p>
    <p>Blue Willow Promotions Group, Inc. provides high-perceived value promotional incentives to businesses that want to advertise an exciting Give Away that will instantly attract more customers from your existing advertising efforts.</p>
    <p>Your business can give away incentive certificates that are redeemable for luxury hotel &amp; resort stays with airfare included, cruises, cash for gas, groceries, dining and even electronic goods.</p>
  </div>
  <div class="samples-art" role="img" aria-label="Fanned stack of sample incentive certificates for cruises, cash back, travel and electronics"></div>
</section>

<section class="how">
  <h2 class="section-title">How Can We Do It?</h2>
  <div class="how-copy">
    <p>We help fill empty rooms for thousands of hotels and resorts in hundreds of destinations around the world as well as the major cruise lines. Hotels and resorts are rarely full so when we place someone in their empty rooms, they end up making it up when travelers spend money on room service, spa services, eat at their in-house restaurants, casino and take advantage of other amenities that drive revenue.</p>
    <p>We also help over 18,000 restaurants, electronic manufacturers, the major gas companies and top grocery chains in the U.S and Canada increase brand awareness as well as increase customer loyalty.</p>
  </div>
</section>

<section class="testimonials">
  <h2 class="section-title">Testimonials</h2>
  <span class="quote-mark quote-open">&ldquo;</span>
  <p class="quote-text">I began using your incentives two years ago to boost lead generation efforts. I have experienced a 63% increase in lead captures. And, even more importantly, my sales have increased as well. The ability to offer unlimited certificates and not having to pay for each certificate I give away is perhaps the best feature of the program, but having the flexibility to email or print certificates for my customers is also wonderful. I even use your html banners to automate my promotions right on my website!.</p>
  <span class="quote-mark quote-close">&rdquo;</span>
  <p class="quote-name">Dana R.</p>
  <p class="quote-place">Cedar Hollow, TN</p>
</section>

<footer class="site-footer">© 2017 &nbsp;Blue Willow Promotions Group, Inc. - All Rights Reserved</footer>

</body>
</html>
```